Brand new website for global research and investment startup

We need a simple website, maybe 3 pages: landing page with business description, investment philosophy, team and contact info.
We have a logo already that can be incorporated. Please use the logo only, not the text
We like the color green, something along the lines of #3D6C32 as the main color.
We'd like to design the website with geometric shapes in gradations of the base color. The shapes should suggest "work in progress", "built to last (a long time)", "solidity" and "indestructibility". One idea floating in my head sees smaller features with icosahedron and dodecahedron shapes, and maybe larger structures like crystal lattices; but please feel free to be creative and imagine your own.

```html
<!DOCTYPE html>
<html lang="en">
<head>
<meta charset="utf-8">
<title>Research Journal — Ridgeline Research &amp; Investment</title>
<link href="https://fonts.googleapis.com/css2?family=Catamaran:wght@400;500;600;700;800&display=swap" rel="stylesheet">
<style>
  :root {
    --green-900: #13221a;
    --green-800: #1b3320;
    --green-700: #2f5b2a;
    --green-600: #3d6c32;
    --green-500: #3f9a3a;
    --green-300: #7fae77;
    --ink: #172519;
    --muted: #6b736c;
    --line: #e3e7e1;
    --hero-bg: #f8faf6;
    --section-bg: #f4f6f2;
    --white: #ffffff;
  }
  * { box-sizing: border-box; margin: 0; padding: 0; }
  html, body { width: 1200px; height: 1200px; overflow: hidden; background: var(--white); }
  body { font-family: "Catamaran", "Segoe UI", sans-serif; color: var(--ink); }

  .page { position: absolute; left: 99px; top: 0; width: 1002px; height: 1200px; background: var(--white); overflow: hidden; }

  /* Header */
  .site-header { position: absolute; top: 0; left: 0; width: 100%; height: 46px; background: var(--hero-bg); border-bottom: 1px solid #eef1ec; z-index: 2; }
  .brand { position: absolute; left: 169px; top: 13px; display: flex; align-items: center; gap: 6px; font-size: 14px; font-weight: 700; color: var(--green-700); letter-spacing: -0.01em; }
  .brand-dot { width: 10px; height: 10px; border-radius: 50%; background: var(--green-700); }
  .nav { position: absolute; top: 0; left: 519px; height: 46px; font-size: 8.6px; color: var(--ink); }
  .nav a { color: inherit; text-decoration: none; position: absolute; white-space: nowrap; top: 17px; }
  .nav .is-active::after { content: ""; position: absolute; left: 0; right: 0; bottom: -4px; height: 1px; background: var(--green-500); }
  .btn-outline { position: absolute; left: 731px; top: 10.5px; width: 102px; height: 25px; border: 1px solid var(--green-800); border-radius: 13px; font-size: 8px; font-weight: 700; color: var(--green-800); display: flex; align-items: center; justify-content: center; text-decoration: none; padding-top: 1px; }

  /* Hero */
  .hero { position: absolute; top: 47px; left: 0; width: 100%; height: 263px; background: linear-gradient(180deg, var(--hero-bg), #fbfcfa); }
  .hero-band { position: absolute; top: 310px; left: 0; width: 100%; height: 46px; background: var(--white); border-bottom: 1px solid #e9ece7; }
  .hero-lattice { position: absolute; left: 640px; top: 58px; width: 240px; height: 260px; }
  .hero-copy { position: absolute; left: 169px; top: 0; width: 664px; height: 356px; }
  .eyebrow { position: absolute; top: 97px; display: flex; align-items: center; gap: 7px; font-size: 7px; font-weight: 700; letter-spacing: 0.18em; color: var(--green-700); }
  .eyebrow::before { content: ""; width: 18px; height: 1px; background: var(--green-500); }
  .hero-title { position: absolute; top: 120px; font-size: 51px; font-weight: 500; line-height: 45.5px; letter-spacing: -0.035em; color: var(--ink); width: 470px; }
  .hero-lede { position: absolute; top: 266px; width: 380px; font-size: 11.2px; line-height: 15.5px; color: var(--muted); }

  /* Journal grid */
  .journal { position: absolute; top: 356px; left: 0; width: 100%; height: 675px; background: var(--section-bg); }
  .grid { position: absolute; top: 64px; left: 169px; width: 664px; display: grid; grid-template-columns: 326px 326px; column-gap: 11px; row-gap: 11px; }
  .card { position: relative; height: 175px; background: var(--white); border: 1px solid #e8ebe6; border-radius: 10px; padding: 20px 16px 0; }
  .card-tag { font-size: 6.6px; font-weight: 800; letter-spacing: 0.12em; color: var(--green-500); text-transform: uppercase; }
  .card-title { margin-top: 8px; font-size: 15.5px; line-height: 16.5px; font-weight: 600; letter-spacing: -0.02em; color: var(--ink); }
  .card-text { margin-top: 6px; font-size: 9.6px; line-height: 13px; color: var(--muted); }
  .card-foot { position: absolute; left: 16px; right: 16px; top: 123px; border-top: 1px solid var(--line); height: 51px; display: flex; align-items: center; justify-content: space-between; }
  .card-meta { font-size: 6.8px; color: var(--muted); }
  .card-arrow { width: 21px; height: 21px; border: 1px solid var(--line); border-radius: 50%; display: flex; align-items: center; justify-content: center; }

  /* Footer */
  .site-footer { position: absolute; top: 1031px; left: 0; width: 100%; height: 169px; background: var(--green-900); color: #d7dfd6; }
  .footer-brand { position: absolute; left: 169px; top: 36px; display: flex; align-items: center; gap: 6px; font-size: 15px; font-weight: 700; color: var(--green-500); }
  .footer-brand .brand-dot { background: var(--green-500); width: 11px; height: 11px; }
  .footer-about { position: absolute; left: 169px; top: 79px; width: 190px; font-size: 7.8px; line-height: 11px; color: #a9b5a8; }
  .footer-col { position: absolute; top: 34px; }
  .footer-col h4 { font-size: 6.5px; font-weight: 700; letter-spacing: 0.18em; color: var(--green-300); margin-bottom: 8px; }
  .footer-col a { display: block; font-size: 8.4px; color: #eef2ed; text-decoration: none; line-height: 16px; }
  .footer-rule { position: absolute; left: 169px; width: 664px; top: 127px; height: 1px; background: #28392c; }
  .footer-legal { position: absolute; left: 169px; width: 664px; top: 143px; display: flex; justify-content: space-between; font-size: 6.6px; color: #8c998b; }
</style>
</head>
<body>
<div class="page">
  <header class="site-header">
    <div class="brand"><span class="brand-dot"></span>Ridgeline</div>
    <nav class="nav">
      <a href="#" style="left:0">Home</a>
      <a href="#" style="left:38px">Philosophy</a>
      <a href="#" class="is-active" style="left:92px">Research</a>
      <a href="#" style="left:139px">Team &amp; Contact</a>
    </nav>
    <a class="btn-outline" href="#">Request a conversation</a>
  </header>

  <section class="hero"></section>
  <div class="hero-band"></div>

  <svg class="hero-lattice" viewBox="0 0 240 260" aria-hidden="true">
    <g fill="none" stroke="#3d6c32" stroke-width="0.8">
      <g stroke-opacity="0.16">
        <path d="M40 60 L100 30 L160 60 L160 130 L100 160 L40 130 Z"/>
        <path d="M100 160 L160 130 L220 160 L220 230 L160 260"/>
        <path d="M40 130 L100 160 L100 230"/>
        <path d="M100 30 L100 100 L160 130 M100 100 L40 130"/>
        <path d="M160 60 L220 30 L220 100 L160 130 M220 100 L220 160"/>
      </g>
      <g stroke-opacity="0.28">
        <path d="M150 190 L178 176 L200 192 L192 220 L162 222 Z"/>
        <path d="M150 190 L176 200 L200 192 M176 200 L192 220 M176 200 L162 222 M176 200 L178 176"/>
      </g>
    </g>
    <g fill="#3d6c32" fill-opacity="0.22">
      <circle cx="40" cy="60" r="2"/><circle cx="100" cy="30" r="2"/><circle cx="160" cy="60" r="2"/>
      <circle cx="160" cy="130" r="2"/><circle cx="100" cy="160" r="2"/><circle cx="40" cy="130" r="2"/>
      <circle cx="100" cy="100" r="2"/><circle cx="220" cy="30" r="2"/><circle cx="220" cy="100" r="2"/>
      <circle cx="220" cy="160" r="2"/><circle cx="100" cy="230" r="2"/>
    </g>
  </svg>

  <div class="hero-copy">
    <p class="eyebrow">RESEARCH JOURNAL</p>
    <h1 class="hero-title">Notes for thinking, not content for content's sake.</h1>
    <p class="hero-lede">A deliberately small journal for frameworks, investment questions and research observations worth returning to.</p>
  </div>

  <section class="journal">
    <div class="grid">
      <article class="card">
        <p class="card-tag">Research note</p>
        <h2 class="card-title">When the market prices the story but misses the structure.</h2>
        <p class="card-text">A framework for separating headline momentum from durable business economics.</p>
        <div class="card-foot"><span class="card-meta">Long-form note</span><span class="card-arrow"><svg width="7" height="7" viewBox="0 0 7 7"><path d="M1 6L6 1M2.5 1H6V4.5" fill="none" stroke="#6b736c" stroke-width="0.8"/></svg></span></div>
      </article>
      <article class="card">
        <p class="card-tag">Perspective</p>
        <h2 class="card-title">What changes a thesis?</h2>
        <p class="card-text">Five questions that matter more than quarterly noise.</p>
        <div class="card-foot"><span class="card-meta">6 min read</span><span class="card-arrow"><svg width="7" height="7" viewBox="0 0 7 7"><path d="M1 6L6 1M2.5 1H6V4.5" fill="none" stroke="#6b736c" stroke-width="0.8"/></svg></span></div>
      </article>
      <article class="card">
        <p class="card-tag">Field note</p>
        <h2 class="card-title">Patience is not passivity.</h2>
        <p class="card-text">Long-horizon ownership still requires active verification.</p>
        <div class="card-foot"><span class="card-meta">4 min read</span><span class="card-arrow"><svg width="7" height="7" viewBox="0 0 7 7"><path d="M1 6L6 1M2.5 1H6V4.5" fill="none" stroke="#6b736c" stroke-width="0.8"/></svg></span></div>
      </article>
      <article class="card">
        <p class="card-tag">Framework</p>
        <h2 class="card-title">Good business, bad price.</h2>
        <p class="card-text">Why quality alone is not an investment thesis.</p>
        <div class="card-foot"><span class="card-meta">7 min read</span><span class="card-arrow"><svg width="7" height="7" viewBox="0 0 7 7"><path d="M1 6L6 1M2.5 1H6V4.5" fill="none" stroke="#6b736c" stroke-width="0.8"/></svg></span></div>
      </article>
      <article class="card">
        <p class="card-tag">Research process</p>
        <h2 class="card-title">The variable that matters.</h2>
        <p class="card-text">How to identify the one or two drivers with disproportionate impact.</p>
        <div class="card-foot"><span class="card-meta">5 min read</span><span class="card-arrow"><svg width="7" height="7" viewBox="0 0 7 7"><path d="M1 6L6 1M2.5 1H6V4.5" fill="none" stroke="#6b736c" stroke-width="0.8"/></svg></span></div>
      </article>
      <article class="card">
        <p class="card-tag">Perspective</p>
        <h2 class="card-title">Why fewer decisions can be better decisions.</h2>
        <p class="card-text">A note on attention, turnover and research depth.</p>
        <div class="card-foot"><span class="card-meta">5 min read</span><span class="card-arrow"><svg width="7" height="7" viewBox="0 0 7 7"><path d="M1 6L6 1M2.5 1H6V4.5" fill="none" stroke="#6b736c" stroke-width="0.8"/></svg></span></div>
      </article>
    </div>
  </section>

  <footer class="site-footer">
    <div class="footer-brand"><span class="brand-dot"></span>Ridgeline</div>
    <p class="footer-about">Independent research and investment thinking for select professional investors.</p>
    <div class="footer-col" style="left:457px">
      <h4>EXPLORE</h4>
      <a href="#">Investment philosophy</a>
      <a href="#">Research journal</a>
    </div>
    <div class="footer-col" style="left:658px">
      <h4>CONTACT</h4>
      <a href="#">Request a conversation</a>
    </div>
    <div class="footer-rule"></div>
    <div class="footer-legal"><span>© 2026 Ridgeline Research &amp; Investment</span><span>Placeholder content for design presentation</span></div>
  </footer>
</div>
</body>
</html>
```